Tech business card design

We need an amazing business card design for our new business 'Brakka' a marketing tech startup based in Sydney, Australia. We provide an online marketplace for businesses to search and buy advertising media, connect with service providers and learn more about marketing. We wish to communicate 'cool tech', reliability and professionalism and design based around our logo.

Target Market(s)

Business Owners

Contact Information for Business Card

Name
Position
Email Address
Website
Phone Number

Font styles to use
Other font styles liked:
• Avenir & Avenir Next

Colors

Designer to choose colors to be used in the design.

```html
<!DOCTYPE html>
<html lang="en">
<head>
<meta charset="utf-8">
<title>Brakka Business Card</title>
<link rel="stylesheet" href="https://fonts.googleapis.com/css2?family=Nunito+Sans:wght@400;700;800;900&display=swap">
<style>
  :root {
    --page-bg: #e4e4e5;
    --navy: #16103b;
    --navy-light: #241d52;
    --card-white: #f4f4f5;
    --ink: #16103b;
    --ink-soft: #2a2550;
    --logo-white: #f2f2f6;
  }
  * { margin: 0; padding: 0; box-sizing: border-box; }
  html, body {
    width: 1200px; height: 960px; overflow: hidden;
    background: var(--page-bg);
    font-family: "Nunito Sans", Arial, sans-serif;
  }
  .card {
    position: absolute;
    left: 334px;
    width: 535px;
    height: 326px;
    overflow: hidden;
  }
  .card--front { top: 139px; background: var(--navy); }
  .card--back { top: 510px; background: var(--card-white); }

  .circuit-area {
    position: absolute; inset: 0;
    background: radial-gradient(circle at 62% 50%, var(--navy-light) 0%, var(--navy) 62%);
  }
  .front-wordmark {
    position: absolute;
    left: 0; right: 0; top: 0; bottom: 0;
    display: flex; align-items: center; justify-content: center;
    color: var(--logo-white);
    font-weight: 900;
    font-size: 66px;
    letter-spacing: -1px;
  }

  .holder { position: absolute; left: 41px; top: 106px; color: var(--ink); }
  .holder__name { font-weight: 800; font-size: 19px; letter-spacing: 0.3px; line-height: 1.1; }
  .holder__role { font-weight: 400; font-size: 14px; letter-spacing: 0.3px; margin-top: 2px; }

  .contacts { position: absolute; left: 41px; top: 230px; list-style: none; color: var(--ink-soft); }
  .contacts li {
    display: flex; align-items: center; gap: 5px;
    font-size: 13.5px; line-height: 18px; letter-spacing: 0.2px;
  }
  .contacts svg { width: 11px; height: 11px; flex: none; }

  .side-wordmark {
    position: absolute;
    left: 463px; top: 164px;
    transform: translate(-50%, -50%) rotate(-90deg);
    color: var(--ink);
    font-weight: 900;
    font-size: 74px;
    letter-spacing: -1px;
    line-height: 1;
    white-space: nowrap;
  }
</style>
</head>
<body>
  <section class="card card--front">
    <div class="circuit-area" role="img" aria-label="Faint circuit-board line pattern radiating from a circle"></div>
    <div class="front-wordmark">Brakka</div>
  </section>

  <section class="card card--back">
    <div class="holder">
      <p class="holder__name">MARCUS REID</p>
      <p class="holder__role">FOUNDER, DIRECTOR</p>
    </div>
    <ul class="contacts">
      <li>
        <svg viewBox="0 0 12 12" fill="none" stroke="currentColor" stroke-width="1.2"><rect x="3" y="0.8" width="6" height="10.4" rx="1"/><line x1="5" y1="9.6" x2="7" y2="9.6"/></svg>
        +61 (0)400 555 182
      </li>
      <li>
        <svg viewBox="0 0 12 12" fill="none" stroke="currentColor" stroke-width="1.2"><rect x="0.8" y="2.2" width="10.4" height="7.6"/><polyline points="0.8,2.2 6,6.6 11.2,2.2"/></svg>
        marcus@brakkamedia.com.au
      </li>
      <li>
        <svg viewBox="0 0 12 12" fill="none" stroke="currentColor" stroke-width="1.1"><circle cx="6" cy="6" r="5.2"/><ellipse cx="6" cy="6" rx="2.3" ry="5.2"/><line x1="0.8" y1="6" x2="11.2" y2="6"/></svg>
        www.brakkamedia.com.au
      </li>
    </ul>
    <div class="side-wordmark">Brakka</div>
  </section>
</body>
</html>
```